Consultative Employee Benifits Firm Needs Business Card Design Project

We need a business card design for a new company based in Northern Virginia called "Telman Financial Services, LLC. We are both a wealth management advisory firm, as well as an employee benefits firm, which strives to provide superior creativity in employee benefits plan design and greater client and employee satisfaction. We are obsessed with service and follow up.

Our firm specializes in the areas of group health, life, dental, disability, voluntary benefits, Executive Benefits, HRA and HSA programs. We offer competitive employee benefit packages and pricing models for single or multi-state/multi location companies by maintaining preferred relationships with a large number of regional and national carriers.

Our firm also considers the many dimensions of your wealth through an integrated process we call wealth structuring — a comprehensive, dynamic approach to building, preserving, enjoying and transferring your wealth. And because we are often dealing with complex ownership structures and complicated, changing family dynamics, we bring the highest level of experience and creativity to managing your wealth. We work hard to help ensure that your legacy lasts by preparing your children for the financial challenges and opportunities that are headed their way.

Our final design should communicate an integrated approach to finanial safety and optimization
Updates

 Due to a few designers not accepting due to low budget, I have increased budget payout 19%. 

Project Deadline Extended
Reason: I have only heard from 12 designers. So, maybe I did not give the right amount of time to do the project. For the designers that have submitted their designs, thank you. I have seen three or four designs that I liked and might end up with one of them after it's all over, but I thought I would see between 20 - 25 before everything was over. Dan

Target Market(s)

Professionals; doctors, contractors, small to mid size business owners, ages 50 -65 with nert worth of 2MM

Industry/Entity Type

Financial

Requirements
Must have
• Telman Financial Services, LLC

Dan Telman
President
41957 Marwick Hollow Street
Quenford Glen, 20871

Office: 703 555-0184
Cell: 703 555-0127
Fax: 703 555-0163
Email: dantelman@quorvex.net
Should not have
• No pink or yellow colors.
No generic clipart (coins, dollar signs, money bags, graphs)

```html
<!DOCTYPE html>
<html lang="en">
<head>
<meta charset="utf-8">
<title>Telman Financial Services, LLC — Business Card</title>
<link rel="stylesheet" href="https://fonts.googleapis.com/css2?family=Tinos:wght@400;700&display=swap">
<style>
  :root {
    --navy: #133c68;
    --gold: #b48a12;
    --paper: #ffffff;
    --backdrop: #f1f2f4;
    --card-w: 520px;
    --card-h: 300px;
    --band-h: 140px;
    --bar-w: 12px;
  }
  * { box-sizing: border-box; margin: 0; padding: 0; }
  html, body { width: 1200px; height: 1200px; overflow: hidden; }
  body {
    background: var(--backdrop);
    font-family: "Tinos", "Times New Roman", serif;
    color: var(--navy);
    display: flex;
    align-items: center;
    justify-content: center;
    gap: 60px;
  }
  .card {
    position: relative;
    width: var(--card-w);
    height: var(--card-h);
    background: var(--paper);
    box-shadow: 0 6px 18px rgba(19, 60, 104, 0.14);
    overflow: hidden;
  }

  /* Front */
  .brand {
    position: absolute;
    left: 16px;
    top: 34px;
    display: flex;
    align-items: center;
    gap: 10px;
  }
  .brand-dot {
    width: 50px;
    height: 50px;
    border-radius: 50%;
    background: var(--navy);
  }
  .brand-name {
    font-weight: 700;
    font-size: 21px;
    line-height: 1.1;
    color: var(--navy);
    text-transform: uppercase;
    text-align: center;
  }
  .brand-name .brand-sub { display: block; font-size: 13px; letter-spacing: 0.5px; }
  .name-panel {
    position: absolute;
    right: 0;
    top: 0;
    width: 37%;
    height: var(--band-h);
    background: var(--navy);
    color: #fff;
    display: flex;
    flex-direction: column;
    justify-content: flex-end;
    align-items: center;
    padding-bottom: 22px;
  }
  .person-name { font-weight: 700; font-size: 23px; text-transform: uppercase; letter-spacing: 0.3px; }
  .person-title { font-weight: 700; font-size: 10px; text-transform: uppercase; letter-spacing: 0.8px; margin-top: 2px; }
  .gold-bar {
    position: absolute;
    left: 0;
    top: var(--band-h);
    bottom: 0;
    width: var(--bar-w);
    background: var(--gold);
  }
  .address {
    position: absolute;
    left: 30px;
    top: 210px;
    font-size: 16px;
    line-height: 1.35;
  }
  .contact {
    position: absolute;
    right: 14px;
    top: 194px;
    font-size: 14px;
    line-height: 1.38;
    text-align: right;
  }

  /* Back */
  .back-title {
    position: absolute;
    left: 0;
    right: 0;
    top: 42px;
    text-align: center;
    font-weight: 700;
    font-size: 26px;
    line-height: 1.15;
    color: var(--navy);
    text-transform: uppercase;
  }
  .back-title .brand-sub { display: block; font-size: 16px; letter-spacing: 0.6px; }
  .back-band {
    position: absolute;
    left: 0;
    right: 0;
    bottom: 0;
    top: var(--band-h);
    background: var(--navy);
  }
  .back-band .gold-bar { top: 0; }
  .back-mark {
    position: absolute;
    left: 50%;
    top: 50%;
    width: 120px;
    height: 120px;
    transform: translate(-50%, -50%);
  }
</style>
</head>
<body>
  <section class="card card-front" aria-label="Business card front">
    <div class="brand">
      <span class="brand-dot" aria-hidden="true"></span>
      <p class="brand-name">Telman Financial<span class="brand-sub">Services, LLC</span></p>
    </div>
    <div class="name-panel">
      <p class="person-name">Dan Telman</p>
      <p class="person-title">President</p>
    </div>
    <div class="gold-bar"></div>
    <address class="address" style="font-style:normal">
      41957 Marwick Hollow Street<br>
      Quenford Glen, 20871
    </address>
    <p class="contact">
      Office: 703 555-0184<br>
      Cell: 703 555-0127<br>
      Fax: 703 555-0163<br>
      Email: dantelman@quorvex.net
    </p>
  </section>

  <section class="card card-back" aria-label="Business card back">
    <p class="back-title">Telman Financial<span class="brand-sub">Services, LLC</span></p>
    <div class="back-band">
      <div class="gold-bar"></div>
      <svg class="back-mark" viewBox="0 0 120 120" aria-hidden="true">
        <circle cx="60" cy="60" r="56" fill="#ffffff"/>
      </svg>
    </div>
  </section>
</body>
</html>
```